Legal Agribusiness Capability Brochure Design

Design A4 sized 6 page Legal Agribusiness Capability Brochure. Design is to be consistent with current marketing materials - logo, letterhead, website and business card to be provided.
Cover page - Firm name and logo, Agribusiness Capability Statement heading with image 1 below
Inside cover page - About Us section with image 2 below then Awards section below image
Inside middle page - Our Expertise with image 3 below
Inside back page - Our Experience with image 4 below
Back page - Senior Lawyers with image 5 below
Outside Middle Back Page - Contact Us with image 6
Updates

To provide more details to designers for brochure

Target Market(s)

Agribusiness - Australia

Industry/Entity Type

Legal

Colors

Designer to choose colors to be used in the design.

Requirements
Must have
• Use content from uloaded file - Agribusiness Brochure Content
• Use images uploaded
• Professional appearance
• Consistent with current marketing and website https://tallowcreeklegal.com.au/

```html
<!DOCTYPE html>
<html lang="en">
<head>
<meta charset="utf-8">
<title>Tallow Creek Legal – Agribusiness Capability Statement</title>
<link rel="stylesheet" href="https://fonts.googleapis.com/css2?family=Montserrat:wght@400;600;700;800&family=Open+Sans:wght@400;600&display=swap">
<style>
  :root{
    --blue:#1b8ad3;
    --blue-dark:#1572b0;
    --ink:#2b2f33;
    --grey:#6b7178;
    --light:#f4f6f8;
    --paper:#ffffff;
    --stage:#e8e9eb;
    --photo-a:#d9d9d9;
    --photo-b:#4a4a4a;
  }
  *{box-sizing:border-box;margin:0;padding:0}
  html,body{width:1200px;height:2428px;overflow:hidden}
  body{background:var(--stage);position:relative;font-family:"Open Sans",Arial,sans-serif;color:var(--ink)}
  .panel{position:absolute;width:340px;height:720px;background:var(--paper);overflow:hidden}
  .spread{position:absolute;width:1020px;height:720px;left:90px;box-shadow:0 6px 18px rgba(0,0,0,.12)}
  .spread .panel{top:0}
  .spread .panel + .panel{border-left:1px solid #e3e6e9}
  .cover-solo{left:430px;top:67px;box-shadow:0 6px 18px rgba(0,0,0,.12)}
  .outside{top:854px}
  .inside{top:1641px}

  .photo{position:absolute;background:linear-gradient(160deg,var(--photo-a),var(--photo-b))}
  .brand{display:flex;align-items:center;gap:6px;font-family:"Montserrat",Arial,sans-serif;font-weight:700;font-size:10px;color:var(--blue);text-transform:uppercase;letter-spacing:.04em}
  .brand .dot{width:12px;height:12px;border-radius:50%;background:var(--blue)}
  .brand.white{color:#fff}
  .brand.white .dot{background:#fff}

  /* cover */
  .cover .top-mark{position:absolute;right:18px;top:26px}
  .cover .photo{left:0;top:70px;width:340px;height:330px}
  .cover .band{position:absolute;left:0;top:400px;width:340px;height:320px;background:var(--blue)}
  .cover .band::before{content:"";position:absolute;left:0;top:0;width:340px;height:26px;background:var(--blue-dark)}
  .cover .logo-box{position:absolute;left:22px;top:46px;background:#fff;padding:9px 12px}
  .cover .title{position:absolute;left:22px;top:118px;font-family:"Montserrat",Arial,sans-serif;font-weight:800;font-size:33px;color:#fff;letter-spacing:.01em}
  .cover .subtitle{position:absolute;left:22px;top:160px;font-family:"Montserrat",Arial,sans-serif;font-weight:600;font-size:12px;color:#fff;letter-spacing:.25em}

  .heading{font-family:"Montserrat",Arial,sans-serif;font-weight:700;font-size:14px;color:var(--blue);text-transform:uppercase;letter-spacing:.05em}
  .body-text{font-size:8.5px;line-height:1.55;color:var(--grey)}

  /* senior lawyers */
  .lawyers{padding:34px 26px}
  .lawyer{display:flex;gap:12px;margin-top:26px}
  .lawyer .portrait{flex:0 0 46px;height:46px;border-radius:50%;background:linear-gradient(160deg,#c9cdd1,#6e747a)}
  .lawyer h3{font-family:"Montserrat",Arial,sans-serif;font-size:11px;font-weight:700;color:var(--ink)}
  .lawyer .role{font-size:8.5px;color:var(--blue);margin:2px 0 6px;font-weight:600}
  .foot-band{position:absolute;left:0;bottom:0;width:340px;height:70px;background:var(--blue);display:flex;align-items:center;padding:0 22px}

  /* contact */
  .contact{text-align:center;padding-top:170px}
  .contact .rule{width:40px;height:3px;background:var(--blue);margin:10px auto 26px}
  .contact-item{margin:0 auto 22px;width:220px}
  .contact-item svg{display:block;margin:0 auto 6px}
  .contact-item p{font-size:9px;color:var(--ink);line-height:1.5}

  /* about */
  .about{padding:30px 24px}
  .about .photo{left:0;top:300px;width:340px;height:170px}
  .about .awards{position:absolute;left:24px;top:492px;width:292px}
  .tick-list{list-style:none;margin-top:10px}
  .tick-list li{display:flex;gap:8px;align-items:flex-start;font-size:8.5px;color:var(--grey);margin-bottom:9px;line-height:1.45}
  .tick-list svg{flex:0 0 11px;margin-top:1px}

  /* middle inside */
  .mid .blue-top{position:absolute;left:0;top:0;width:340px;height:250px;background:var(--blue);padding:36px 26px;color:#fff}
  .mid .blue-top .heading{color:#fff}
  .mid .blue-top p{font-size:8.5px;line-height:1.6;margin-top:12px;color:#eaf4fb}
  .mid .photo{left:0;top:250px;width:340px;height:470px;background:linear-gradient(170deg,#cfcfcf,#7a7a7a 55%,#3c3c3c)}

  /* expertise */
  .expertise{padding:34px 24px}
  .exp-item{background:var(--blue);color:#fff;margin-top:12px;padding:10px 12px;display:flex;gap:10px;align-items:center}
  .exp-item .num{font-family:"Montserrat",Arial,sans-serif;font-weight:800;font-size:14px;width:22px}
  .exp-item h4{font-family:"Montserrat",Arial,sans-serif;font-size:10px;font-weight:700}
  .exp-item p{font-size:8px;color:#e3f0fa;margin-top:2px}
</style>
</head>
<body>

<!-- front cover -->
<section class="panel cover cover-solo">
  <div class="brand top-mark"><span class="dot"></span>Tallow Creek Legal</div>
  <div class="photo" role="img" aria-label="Black and white photo of a farmer standing in a paddock"></div>
  <div class="band">
    <div class="logo-box"><div class="brand"><span class="dot"></span>Tallow Creek Legal</div></div>
    <h1 class="title">AGRIBUSINESS</h1>
    <p class="subtitle">CAPABILITY STATEMENT</p>
  </div>
</section>

<!-- outside spread -->
<div class="spread outside">
  <section class="panel lawyers" style="left:0">
    <h2 class="heading">Senior Lawyers</h2>
    <div class="lawyer">
      <div class="portrait" role="img" aria-label="Portrait of senior lawyer"></div>
      <div>
        <h3>Andrew Harlow</h3>
        <p class="role">Principal Lawyer</p>
        <p class="body-text">Andrew advises farming families and rural businesses on property transactions, succession planning, water rights and commercial agreements across regional Australia.</p>
      </div>
    </div>
    <div class="lawyer">
      <div class="portrait" role="img" aria-label="Portrait of senior lawyer"></div>
      <div>
        <h3>Claire Denton</h3>
        <p class="role">Senior Associate</p>
        <p class="body-text">Claire works with primary producers on leasing, finance, disputes and estate matters, bringing practical advice grounded in country life.</p>
      </div>
    </div>
    <div class="foot-band"><div class="brand white"><span class="dot"></span>Tallow Creek Legal</div></div>
  </section>

  <section class="panel contact" style="left:340px">
    <h2 class="heading">Contact Us</h2>
    <div class="rule"></div>
    <div class="contact-item">
      <svg width="18" height="18" viewBox="0 0 24 24"><path fill="#1b8ad3" d="M6.6 10.8a15 15 0 0 0 6.6 6.6l2.2-2.2a1 1 0 0 1 1-.25 11.4 11.4 0 0 0 3.6.6 1 1 0 0 1 1 1V20a1 1 0 0 1-1 1A17 17 0 0 1 3 4a1 1 0 0 1 1-1h3.5a1 1 0 0 1 1 1c0 1.25.2 2.45.6 3.6a1 1 0 0 1-.25 1z"/></svg>
      <p>(02) 5550 1842</p>
    </div>
    <div class="contact-item">
      <svg width="18" height="18" viewBox="0 0 24 24"><path fill="#1b8ad3" d="M12 2a7 7 0 0 0-7 7c0 5.2 7 13 7 13s7-7.8 7-13a7 7 0 0 0-7-7zm0 9.5A2.5 2.5 0 1 1 12 6.5a2.5 2.5 0 0 1 0 5z"/></svg>
      <p>14 Station Street<br>Wagga Flats NSW 2650</p>
    </div>
    <div class="contact-item">
      <svg width="18" height="18" viewBox="0 0 24 24"><path fill="#1b8ad3" d="M3 5h18v14H3z"/><path fill="none" stroke="#fff" stroke-width="1.6" d="M3.5 5.5 12 12l8.5-6.5"/></svg>
      <p>enquiries@tallowcreeklegal.com.au</p>
    </div>
    <div class="contact-item">
      <svg width="18" height="18" viewBox="0 0 24 24"><circle cx="12" cy="12" r="9" fill="none" stroke="#1b8ad3" stroke-width="2"/><path fill="none" stroke="#1b8ad3" stroke-width="1.5" d="M3 12h18M12 3c3 3 3 15 0 18M12 3c-3 3-3 15 0 18"/></svg>
      <p>https://tallowcreeklegal.com.au/</p>
    </div>
  </section>

  <section class="panel cover" style="left:680px">
    <div class="brand top-mark"><span class="dot"></span>Tallow Creek Legal</div>
    <div class="photo" role="img" aria-label="Black and white photo of a farmer standing in a paddock"></div>
    <div class="band">
      <div class="logo-box"><div class="brand"><span class="dot"></span>Tallow Creek Legal</div></div>
      <h1 class="title">AGRIBUSINESS</h1>
      <p class="subtitle">CAPABILITY STATEMENT</p>
    </div>
  </section>
</div>

<!-- inside spread -->
<div class="spread inside">
  <section class="panel about" style="left:0">
    <h2 class="heading">About Us</h2>
    <p class="body-text" style="margin-top:12px">Tallow Creek Legal is a regional law firm that has supported farming families, rural enterprises and agribusiness operators for more than thirty years. We understand the land, the seasons and the pressures that shape decisions on the farm.</p>
    <p class="body-text" style="margin-top:10px">Our team provides clear, practical advice on property, finance, succession, water, employment and disputes, helping clients protect what they have built and plan for the next generation.</p>
    <div class="photo" role="img" aria-label="Black and white photo of vineyard rows beside a dirt track"></div>
    <div class="awards">
      <h2 class="heading">Awards</h2>
      <ul class="tick-list">
        <li><svg width="11" height="11" viewBox="0 0 12 12"><path fill="none" stroke="#1b8ad3" stroke-width="2" d="M1.5 6.5l3 3 6-7"/></svg>Regional Law Firm of the Year – Finalist</li>
        <li><svg width="11" height="11" viewBox="0 0 12 12"><path fill="none" stroke="#1b8ad3" stroke-width="2" d="M1.5 6.5l3 3 6-7"/></svg>Excellence in Rural Client Service</li>
        <li><svg width="11" height="11" viewBox="0 0 12 12"><path fill="none" stroke="#1b8ad3" stroke-width="2" d="M1.5 6.5l3 3 6-7"/></svg>Leading Agribusiness Advisers – Recognised</li>
      </ul>
    </div>
  </section>

  <section class="panel mid" style="left:340px">
    <div class="blue-top">
      <h2 class="heading">Our Experience</h2>
      <p>We have acted on farm sales and acquisitions, water licence transfers, share farming agreements, family succession plans and rural lending across the state.</p>
      <p>Our clients include graziers, croppers, vignerons, dairy operators and agricultural suppliers who value local knowledge and timely advice.</p>
    </div>
    <div class="photo" role="img" aria-label="Black and white photo of vineyard rows stretching to the horizon"></div>
  </section>

  <section class="panel expertise" style="left:680px">
    <h2 class="heading">Our Expertise</h2>
    <p class="body-text" style="margin-top:10px">We offer a complete range of legal services tailored to the needs of rural and agribusiness clients.</p>
    <div class="exp-item"><span class="num">01</span><div><h4>Rural Property</h4><p>Purchases, sales and leasing of farmland</p></div></div>
    <div class="exp-item"><span class="num">02</span><div><h4>Succession Planning</h4><p>Wills, trusts and family farm transfers</p></div></div>
    <div class="exp-item"><span class="num">03</span><div><h4>Water Rights</h4><p>Licences, allocations and trading</p></div></div>
    <div class="exp-item"><span class="num">04</span><div><h4>Finance &amp; Lending</h4><p>Securities, refinancing and debt advice</p></div></div>
    <div class="exp-item"><span class="num">05</span><div><h4>Commercial Agreements</h4><p>Share farming, supply and contracts</p></div></div>
    <div class="exp-item"><span class="num">06</span><div><h4>Disputes</h4><p>Boundary, contract and family matters</p></div></div>
  </section>
</div>

</body>
</html>
```